Bref créative
T&R FINANCIAL SERVICE
"Where Your Concern Is Our Focus"
Professional
Marisol Quade
2417 Birchwood Lane, Suite 208
P.O. Box 3782
Ridgemont, GA 36197
support@trfinancialgroup.example
trfinancialgroup.example
please incorporate center logo from the website (the one with the green and black writing) thanks
for those who needed ai

```html
<!DOCTYPE html>
<html lang="en">
<head>
<meta charset="utf-8">
<title>T&amp;R Financial Service – Business Card</title>
<link rel="stylesheet" href="https://fonts.googleapis.com/css2?family=Arimo:wght@400;700&display=swap">
<style>
  :root {
    --card-bg: #ffffff;
    --ink: #1f1f1f;
    --brand-green: #4f9a1c;
    --brand-green-bright: #7cc242;
    --brand-green-dark: #1d4a0c;
    --brand-green-deep: #0f2a05;
  }
  html, body {
    margin: 0;
    padding: 0;
    overflow: hidden;
    background: var(--card-bg);
  }
  .business-card {
    position: relative;
    width: 1200px;
    height: 686px;
    background: var(--card-bg);
    overflow: hidden;
    font-family: "Arimo", Arial, sans-serif;
    color: var(--ink);
  }
  .brand {
    position: absolute;
    left: 60px;
    top: 200px;
    width: 460px;
    display: flex;
    align-items: center;
    gap: 20px;
  }
  .brand-dot {
    flex: none;
    width: 44px;
    height: 44px;
    border-radius: 50%;
    background: var(--brand-green);
  }
  .brand-name {
    margin: 0;
    font-size: 38px;
    line-height: 1.15;
    font-weight: 700;
    color: var(--brand-green);
  }
  .divider {
    position: absolute;
    left: 594px;
    top: 108px;
    width: 4px;
    height: 352px;
    background: linear-gradient(to bottom, rgba(79,154,28,0), var(--brand-green) 25%, var(--brand-green) 75%, rgba(79,154,28,0));
  }
  .contact {
    position: absolute;
    left: 667px;
    top: 106px;
  }
  .contact-name {
    margin: 0 0 124px;
    font-size: 36px;
    font-weight: 400;
    line-height: 1.1;
  }
  .contact-details {
    margin: 0;
    font-style: normal;
    font-size: 26px;
    line-height: 31px;
  }
  .footer-band {
    position: absolute;
    left: 0;
    bottom: 0;
    width: 1200px;
    height: 170px;
    background: linear-gradient(to right, var(--brand-green-deep), var(--brand-green-dark) 50%, var(--brand-green) 85%, var(--brand-green-bright));
  }
</style>
</head>
<body>
  <main class="business-card">
    <div class="brand">
      <span class="brand-dot"></span>
      <p class="brand-name">T&amp;R FINANCIAL SERVICE</p>
    </div>

    <div class="divider"></div>

    <section class="contact">
      <h1 class="contact-name">Marisol Quade</h1>
      <address class="contact-details">
        2417 Birchwood Lane, Suite 208<br>
        P.O. Box 3782<br>
        Ridgemont, GA 36197<br>
        Phone : (706) 555-0148<br>
        Email : support@trfinancialgroup.example<br>
        Web : trfinancialgroup.example
      </address>
    </section>

    <div class="footer-band" role="img" aria-label="Decorative green swoosh bands along the bottom edge"></div>
  </main>
</body>
</html>
```